Wedding Planning and Event Planners website

I am driven by perfection of my occupation and i look forward to having an attractive and contemporary website for an event and wedding planning group. We are located in the United States and Canada and we offer our services only in these two countries. My website is for people who are planning events such Church programs, weddings, musical concerts, Picnic, etc. My website should have imaginary of events such as weddings, musical concerts and picnic, etc.. I don't have any reference website because i want all designers to be creative and unique. I prefer blue,red,green,yellow colors.

Industry/Entity Type

Wedding

Coding

Coded - Design and coding required

```html
<!DOCTYPE html>
<html lang="en">
<head>
<meta charset="utf-8">
<title>Marlow Planners — Wedding &amp; Event Planning</title>
<link href="https://fonts.googleapis.com/css2?family=Montserrat:wght@400;500&family=Open+Sans:wght@400;600&family=Roboto+Slab:wght@300;400&display=swap" rel="stylesheet">
<style>
:root{
  --yellow:#fcc800;
  --yellow-text:#ffd400;
  --red:#ee1111;
  --blue:#1459c9;
  --blue-deep:#0c3fa3;
  --white:#ffffff;
  --grey:#7a7a7a;
  --ink:#333333;
}
*{margin:0;padding:0;box-sizing:border-box}
html,body{width:802px;height:1200px;overflow:hidden;background:var(--white)}
.page{position:relative;width:802px;height:1200px;font-family:"Open Sans",sans-serif}

/* hero */
.hero{position:absolute;left:0;top:0;width:802px;height:383px;
  background:linear-gradient(180deg,#cfc6bc 0%,#ece4dc 35%,#e8dcd4 60%,#f1ebe6 100%)}
.hero-photo{position:absolute;inset:0;
  background:radial-gradient(ellipse at 50% 45%,rgba(120,170,210,.35) 0 12%,transparent 30%),
  linear-gradient(90deg,rgba(110,60,150,.35) 0 8%,transparent 22% 78%,rgba(110,60,150,.35) 92%)}
.brand{position:absolute;left:100px;top:22px;font-family:"Roboto Slab",serif;font-weight:400;font-size:22px;color:var(--white)}
.nav{position:absolute;top:33px;left:353px;display:flex;gap:0}
.nav a{font-family:"Montserrat",sans-serif;font-size:10px;color:var(--white);text-decoration:none;position:absolute;white-space:nowrap}
.nav a.active{color:var(--yellow-text)}
.hero h1{position:absolute;top:166px;left:0;width:802px;text-align:center;font-family:"Roboto Slab",serif;font-weight:400;font-size:30px;line-height:29px;color:var(--white);letter-spacing:.5px}
.btn-book{position:absolute;left:354px;top:237px;width:97px;height:26px;border-radius:13px;background:var(--yellow);color:var(--white);font-family:"Montserrat",sans-serif;font-size:11px;line-height:26px;text-align:center}
.dots{position:absolute;top:356px;left:371px;display:flex;gap:3px}
.dots span{width:11px;height:11px;border-radius:50%;background:var(--white)}
.dots span.open{background:transparent;border:1.5px solid var(--white)}

/* services */
.service{position:absolute;top:404px;width:150px;text-align:center}
.service svg{display:block;margin:0 auto}
.service h3{font-family:"Roboto Slab",serif;font-weight:400;font-size:12.5px;color:var(--red);margin-top:6px}
.service p{font-size:7.4px;line-height:13px;color:var(--grey);margin-top:4px}
.service .btn-more{display:inline-block;margin-top:6px;width:70px;height:19px;background:var(--yellow);color:var(--white);font-family:"Montserrat",sans-serif;font-weight:500;font-size:7.5px;line-height:19px}

/* welcome */
.welcome{position:absolute;left:0;top:588px;width:802px;height:305px}
.welcome-text{position:absolute;left:0;top:0;width:802px;text-align:center;color:var(--white)}
.welcome-text h2{position:absolute;top:84px;width:802px;font-family:"Roboto Slab",serif;font-weight:300;font-size:21px}
.welcome-text .lead{position:absolute;top:122px;width:802px;font-size:10px}
.welcome-text .body{position:absolute;top:147px;left:135px;width:532px;font-size:9.2px;line-height:15.5px}
.btn-outline{position:absolute;top:206px;left:352px;width:98px;height:28px;border:1.5px solid var(--white);border-radius:14px;font-family:"Montserrat",sans-serif;font-size:11px;line-height:25px}

/* gallery */
.gallery-title{position:absolute;top:887px;left:0;width:802px;text-align:center;font-family:"Roboto Slab",serif;font-weight:300;font-size:15.5px;color:var(--ink);letter-spacing:.3px}
.gallery-title::before,.gallery-title::after{content:"";display:inline-block;width:30px;height:1px;background:#bbb;vertical-align:middle;margin:0 8px}
.thumb{position:absolute;top:927px;width:143px;height:101px;border:1px solid #ddd;background:var(--white);padding:4px;box-shadow:0 1px 2px rgba(0,0,0,.15)}
.thumb div{width:100%;height:100%}
.btn-view{position:absolute;top:1043px;left:360px;width:83px;height:24px;border:1.5px solid #bbb;border-radius:12px;text-align:center;font-family:"Roboto Slab",serif;font-size:8px;line-height:21px;color:var(--grey)}

/* footer */
.footer{position:absolute;left:0;top:1100px;width:802px;height:100px;background:var(--yellow)}
.footer-nav{position:absolute;top:41px;left:105px;display:flex;gap:22px}
.footer-nav a{font-family:"Montserrat",sans-serif;font-size:9.5px;color:var(--white);text-decoration:none}
.copy{position:absolute;top:61px;left:105px;font-size:7.6px;color:var(--white)}
.social{position:absolute;top:33px;left:571px;display:flex;gap:5px}
.social span{width:22px;height:22px;border-radius:50%;background:var(--white)}
</style>
</head>
<body>
<div class="page">

  <header class="hero">
    <div class="hero-photo" role="img" aria-label="Wedding hall aisle decorated with flowers, purple ribbons and rose petals"></div>
    <div class="brand">Marlow Planners</div>
    <nav class="nav">
      <a class="active" href="#" style="left:0">HOME</a>
      <a href="#" style="left:53px">ABOUT</a>
      <a href="#" style="left:110px">SERVICES</a>
      <a href="#" style="left:181px">GALLERY</a>
      <a href="#" style="left:247px">PRICE</a>
      <a href="#" style="left:299px">CONTACT</a>
    </nav>
    <h1>WEDDING &amp; EVENT PLANNING<br>IN US &amp; CANADA</h1>
    <div class="btn-book">Book Now</div>
    <div class="dots"><span class="open"></span><span></span><span></span><span></span></div>
  </header>

  <section class="services">
    <div class="service" style="left:100px">
      <svg width="68" height="96" viewBox="0 0 68 96"><path d="M34 95 C28 78 6 62 2 44 A33 33 0 1 1 66 44 C62 62 40 78 34 95Z" fill="var(--red)"/>
        <g fill="none" stroke="#fff" stroke-width="2.4"><rect x="19" y="24" width="30" height="26" rx="3"/><line x1="19" y1="31" x2="49" y2="31"/><line x1="26" y1="20" x2="26" y2="27"/><line x1="42" y1="20" x2="42" y2="27"/></g>
        <path d="M34 46 l-6-6 a3.5 3.5 0 0 1 6-4 a3.5 3.5 0 0 1 6 4z" fill="#fff"/></svg>
      <h3>Wedding Planning</h3>
      <p>Praesent elementum elit at tellus<br>Curabitur metus luctus eu</p>
      <span class="btn-more">READ MORE</span>
    </div>
    <div class="service" style="left:250px">
      <svg width="68" height="96" viewBox="0 0 68 96"><path d="M34 95 C28 78 6 62 2 44 A33 33 0 1 1 66 44 C62 62 40 78 34 95Z" fill="var(--red)"/>
        <g fill="none" stroke="#fff" stroke-width="2.2"><path d="M20 56 V38 L34 26 L48 38 V56Z"/><rect x="30" y="45" width="8" height="11"/><line x1="34" y1="14" x2="34" y2="26"/><line x1="30" y1="18" x2="38" y2="18"/></g></svg>
      <h3>Church Programs</h3>
      <p>Praesent elementum elit at tellus<br>Curabitur metus luctus eu</p>
      <span class="btn-more">READ MORE</span>
    </div>
    <div class="service" style="left:400px">
      <svg width="68" height="96" viewBox="0 0 68 96"><path d="M34 95 C28 78 6 62 2 44 A33 33 0 1 1 66 44 C62 62 40 78 34 95Z" fill="var(--red)"/>
        <g fill="#fff"><path d="M28 22 L46 18 V44 h-2.5 V26 L30.5 29 V48 h-2.5Z"/><ellipse cx="25" cy="48" rx="5" ry="4"/><ellipse cx="41" cy="44" rx="5" ry="4"/></g></svg>
      <h3>Music Concerts</h3>
      <p>Praesent elementum elit at tellus<br>Curabitur metus luctus eu</p>
      <span class="btn-more">READ MORE</span>
    </div>
    <div class="service" style="left:550px">
      <svg width="68" height="96" viewBox="0 0 68 96"><path d="M34 95 C28 78 6 62 2 44 A33 33 0 1 1 66 44 C62 62 40 78 34 95Z" fill="var(--red)"/>
        <g fill="none" stroke="#fff" stroke-width="2.4"><line x1="16" y1="40" x2="52" y2="40"/><line x1="14" y1="47" x2="54" y2="47"/><line x1="22" y1="40" x2="18" y2="54"/><line x1="46" y1="40" x2="50" y2="54"/></g>
        <g fill="#fff"><path d="M22 20 l-5 12 h10z"/><path d="M34 18 l-5 14 h10z"/><path d="M46 20 l-5 12 h10z"/></g></svg>
      <h3>Picnic &amp; Events</h3>
      <p>Praesent elementum elit at tellus<br>Curabitur metus luctus eu</p>
      <span class="btn-more">READ MORE</span>
    </div>
  </section>

  <section class="welcome">
    <svg width="802" height="305" viewBox="0 0 802 305" role="img" aria-label="Blue-tinted banquet tent with decorated tables and chairs">
      <defs><linearGradient id="welcomeFill" x1="0" y1="0" x2="0" y2="1"><stop offset="0" stop-color="#1e6ad8"/><stop offset=".6" stop-color="var(--blue)"/><stop offset="1" stop-color="var(--blue-deep)"/></linearGradient></defs>
      <path d="M0 4 C90 -6 170 40 260 40 C320 40 360 26 390 34 L402 32 L414 34 C450 24 480 40 540 40 C640 40 700 0 802 0 V278 C660 250 560 282 402 284 C240 286 120 260 0 300Z" fill="url(#welcomeFill)"/>
    </svg>
    <div class="welcome-text">
      <h2>Welcome to Marlow Planners</h2>
      <p class="lead">At justo id velit placerat molestie Donec dictum lectus non odio Cras a ante vitae enim</p>
      <p class="body">Pellentesque habitant morbi tristique senectus et netus et malesuada fames ac turpis egestas Cras id elit Integer quis urna Ut ante enim dapibus malesuada fringilla eu condimentum quis Donec convallis pede venenatis nibh Duis quam Nam eget lacus Aliquam erat volutpat Quisque dignissim congue leo Mauris vel lacus</p>
      <div class="btn-outline">Read More</div>
    </div>
  </section>

  <section class="gallery">
    <h2 class="gallery-title">OUR GALLERY</h2>
    <div class="thumb" style="left:103px"><div role="img" aria-label="Beach wedding setup with purple flowers" style="background:linear-gradient(180deg,#7fc4e8 0 35%,#e8e0d0 55%,#b0308f 80%,#c94aa4)"></div></div>
    <div class="thumb" style="left:253px"><div role="img" aria-label="Outdoor banquet tables under thatched umbrellas" style="background:linear-gradient(180deg,#e6e0d6 0 30%,#a88a6a 45%,#d8d4cc 70%,#f0eeea)"></div></div>
    <div class="thumb" style="left:404px"><div role="img" aria-label="Garden wedding aisle with red carpet and white chairs" style="background:linear-gradient(180deg,#6b8f4a 0 25%,#e8ecea 50%,#5e9a3c 85%,#4e8a30)"></div></div>
    <div class="thumb" style="left:554px"><div role="img" aria-label="Music concert stage with purple lights and crowd" style="background:linear-gradient(180deg,#2a1a5e 0,#8a3ad8 40%,#4a2088 70%,#1a1030)"></div></div>
    <div class="btn-view">VIEW MORE</div>
  </section>

  <footer class="footer">
    <nav class="footer-nav">
      <a href="#">HOME</a><a href="#">ABOUT</a><a href="#">SERVICES</a><a href="#">GALLERY</a><a href="#">PRICE</a><a href="#">CONTACT</a>
    </nav>
    <p class="copy">© 2016 Company Name  All right reserved  Term of Use</p>
    <div class="social"><span></span><span></span><span></span><span></span><span></span></div>
  </footer>

</div>
</body>
</html>
```